Business card for Drone Aerial

I need a business card designed keeping in mind I want to do post cards also with a similar design.
Both sides of the card would be cool.
I have a skylark 5 max and would like a picture of it on the front of the card. Similar to one I attached.
I really like the look of a drone in the air and the background pic a little blurry. I attached a few images as IDEAS.
Some special things I want to be on the card additional to the normal business card info:
"Aerial Photography" or "Low Altitude Aerial Photography"?
"ZQB# 90817263"

I like modern and creative. My Favorite color is blue and I like blue on white.
I do not have a business name and am not going to have one. When they read "Aerial Photography" and see the drone and image they will know what the card is for.

FYI, The attached pictures are just images from framewillow and just samples/ideas.

Target Market(s)

Real estate, construction, events

Industry/Entity Type

Business

Contact Information for Business Card

Also Definitely want to contain, my name, my number and email address.

Requirements
Must have
• "ZQB# 90817263"
• "Aerial Photography"

```html
<!DOCTYPE html>
<html lang="en">
<head>
<meta charset="utf-8">
<title>Aerial Photography – Business Card</title>
<link rel="stylesheet" href="https://fonts.googleapis.com/css2?family=Tinos:wght@400;700&family=Saira:wght@500&family=Arimo:wght@400&display=swap">
<style>
  :root {
    --page-bg: #d9d6d0;
    --ink: #111111;
    --paper-white: #ffffff;
    --back-black: #000000;
    --sky-top: #6fa9d8;
    --sky-mid: #bcdcf1;
    --haze: #eef4f7;
    --ridge-far: #8fa2b2;
    --ridge-near: #5d6a52;
    --slope-sun: #8a8a45;
    --drone-light: #e4e8ec;
    --drone-dark: #6b7077;
    --gimbal-light: #d6d9dc;
    --gimbal-dark: #3f4246;
    --glider-grey: #bdbdbd;
  }
  * { margin: 0; padding: 0; box-sizing: border-box; }
  html, body { width: 1200px; height: 933px; overflow: hidden; }
  body { background: var(--page-bg); position: relative; }

  .card {
    position: absolute;
    left: 274px;
    width: 653px;
    height: 374px;
    overflow: hidden;
    box-shadow: 0 4px 14px rgba(0,0,0,0.35);
  }
  .card--front { top: 64px; }
  .card--back { top: 494px; height: 372px; background: var(--back-black); }

  .front__scene {
    position: absolute; inset: 0;
    background: linear-gradient(180deg,
      var(--sky-top) 0%,
      var(--sky-mid) 30%,
      var(--haze) 62%,
      var(--ridge-far) 72%,
      var(--slope-sun) 84%,
      var(--ridge-near) 100%);
  }
  .front__drone {
    position: absolute; left: 46px; top: 32px; width: 250px; height: 196px;
    border-radius: 40px;
    background: radial-gradient(ellipse at 55% 50%, var(--drone-light) 0%, var(--drone-dark) 55%, rgba(107,112,119,0) 72%);
  }
  .front__gimbal {
    position: absolute; left: 496px; top: 232px; width: 124px; height: 142px;
    border-radius: 30px;
    background: radial-gradient(ellipse at 55% 60%, var(--gimbal-light) 0%, var(--gimbal-dark) 55%, rgba(63,66,70,0) 74%);
  }

  .front__title {
    position: absolute; right: 18px; top: 26px;
    font-family: "Tinos", serif; font-weight: 700;
    font-size: 40px; color: var(--ink); line-height: 1;
  }
  .front__name {
    position: absolute; right: 18px; top: 114px;
    font-family: "Saira", sans-serif; font-weight: 500;
    font-size: 28px; color: var(--ink); letter-spacing: 1px; line-height: 1;
  }
  .contact {
    position: absolute; right: 18px;
    display: flex; align-items: center; gap: 14px;
    font-family: "Arimo", sans-serif; font-size: 19.5px; color: var(--ink);
    line-height: 1;
  }
  .contact--phone { top: 160px; }
  .contact--email { top: 183px; }
  .contact--license { top: 206px; right: 45px; }
  .contact__icon { width: 13px; height: 13px; display: block; }

  .back__glider {
    position: absolute; left: 52px; top: 152px; width: 422px; height: 14px;
    background: linear-gradient(90deg, rgba(189,189,189,0) 0%, var(--glider-grey) 20%, var(--glider-grey) 80%, rgba(189,189,189,0) 100%);
    opacity: 0.55;
  }
  .back__title {
    position: absolute; left: 152px; top: 177px;
    font-family: "Tinos", serif; font-weight: 400;
    font-size: 58px; color: var(--paper-white); line-height: 1;
  }
</style>
</head>
<body>
  <section class="card card--front">
    <div class="front__scene" role="img" aria-label="Photo of blue sky with light clouds above hazy mountain ridges"></div>
    <div class="front__drone" role="img" aria-label="Photo of a white quadcopter drone with camera gimbal flying in the sky"></div>
    <div class="front__gimbal" role="img" aria-label="Close-up photo of a drone gimbal camera"></div>
    <h1 class="front__title">Aerial Photography</h1>
    <p class="front__name">Dorvanek Plasitra</p>
    <p class="contact contact--phone">
      <span>021 7390 1148</span>
      <svg class="contact__icon" viewBox="0 0 13 13" aria-hidden="true">
        <rect width="13" height="13" fill="#111"/>
        <path d="M2.5 5.5 Q6.5 2 10.5 5.5 L9.5 6.5 L8 5.8 L8 5 Q6.5 4.4 5 5 L5 5.8 L3.5 6.5 Z M4 7 H9 L10 10.5 H3 Z" fill="#fff"/>
      </svg>
    </p>
    <p class="contact contact--email">
      <span>dorv@liftviewaerial.com</span>
      <svg class="contact__icon" viewBox="0 0 13 13" aria-hidden="true">
        <rect width="13" height="13" fill="#111"/>
        <rect x="2.5" y="3.5" width="8" height="6" fill="#fff"/>
        <path d="M2.5 3.5 L6.5 7 L10.5 3.5" fill="none" stroke="#111" stroke-width="1"/>
      </svg>
    </p>
    <p class="contact contact--license"><span>ZQB# 90817263</span></p>
  </section>

  <section class="card card--back">
    <div class="back__glider" role="img" aria-label="White line drawing of a glider aircraft in flight"></div>
    <h2 class="back__title">Aerial Photography</h2>
  </section>
</body>
</html>
```